Compelling Senior Home Care highlight live-in home care and couples care

Compelling High end client who is looking to advertise and highlight their live-in home care and couples care. Their name is Meadowlark Home Health Services and their website is https://www.meadowlarkhhs-example.com/ Please use their current website colors and I attached some examples.

Specs:

Non-Medical Care or
Home Health Grid Ad
3.85w x 3h

Ad should have:
LOGO
WEBSITE
PHONE NUMBER
(BUTTON - Find Out More)
Text Variations:
We Give People the Help They Need to Live in the Place They Love (see example for exact look and feel)
Do you or your loved one need care at home?
Live at home as long as possible!
Caregivers You Can Trust
Caregivers That Come On Time
Caregivers That Live with You
High Level Care
Hours Match Your Needs

PVG is produced in Macintosh platform CS6. Please create your ads in these programs. Please submit
your ads in high-resolution camera-ready PDF, TIF or EPS format: 300 DPI at 100% of printed size, all
colors CMYK, all fonts and graphics embedded. Use POSTSCRIPT TYPE 1 fonts when possible, TRUE TYPE
FONTS may not print correctly. If submitting native files, please include all linked graphics and fonts.
NOTE: if your ad is not produced by the PVG Art Staff, a professional Ad Agency or Design firm, and is
not properly constructed for technical electronic digital printing, the final printed product may not print
correctly and may differ from your screen proof. Please flightcheck your ad before submitting to PVG.
Publisher reserves the right to charge for all costs incurred in preparation of material submitted that
does not meet the Elders Amber Guide digital specifications.
• All colors, logos, and images in your ad need to be CMYK builds at 300 dpi at 100% size
• Construct your file document size to our size specifications and save your PDF to 100% of size

Target Market(s)

Adults taking care of mom and dad

Industry/Entity Type

Home Health Care

Requirements
Nice to have
• PLEASE SEE EXAMPLES
Should not have
• BORING

```html
<!DOCTYPE html>
<html lang="en">
<head>
<meta charset="utf-8">
<title>Meadowlark Home Health Services – Grid Ad</title>
<link href="https://fonts.googleapis.com/css2?family=Nunito+Sans:wght@400;600;700;800;900&family=Pacifico&display=swap" rel="stylesheet">
<style>
  :root {
    --plum: #7b1f60;
    --plum-deep: #6a1752;
    --blush: #f6e5ef;
    --heart-soft: #e4c2d5;
    --ink: #1e1e1e;
    --white: #ffffff;
    --backdrop: #353535;
  }
  * { margin: 0; padding: 0; box-sizing: border-box; }
  html, body {
    width: 1200px; height: 1178px; overflow: hidden;
    background: var(--backdrop);
    font-family: "Nunito Sans", Arial, sans-serif;
  }
  .ad {
    position: absolute; left: 138px; top: 234px;
    width: 924px; height: 720px;
    background: var(--white); overflow: hidden;
  }
  .ad-shapes { position: absolute; left: 0; top: 0; }

  .brand { position: absolute; left: 58px; top: 148px; display: flex; align-items: center; gap: 16px; }
  .brand-mark { width: 66px; height: 66px; background: var(--plum); }
  .brand-name { color: var(--plum); font-weight: 800; line-height: 1; }
  .brand-name .primary { display: block; font-size: 46px; letter-spacing: -0.5px; }
  .brand-name .secondary { display: block; font-size: 19px; margin-top: 8px; letter-spacing: 0.2px; }

  .headline {
    position: absolute; left: 30px; top: 254px;
    font-size: 41px; font-weight: 400; line-height: 46px; color: var(--ink);
  }
  .headline strong { color: var(--plum); font-weight: 900; }

  .rule { position: absolute; left: 30px; width: 456px; height: 2px; background: var(--plum); opacity: .75; }
  .rule.top { top: 364px; }
  .rule.bottom { top: 426px; }

  .tagline {
    position: absolute; left: 30px; top: 368px;
    font-family: "Pacifico", cursive; font-size: 31px; color: var(--plum);
    line-height: 54px; white-space: nowrap;
  }

  .benefits { position: absolute; left: 30px; top: 444px; list-style: none; }
  .benefits li {
    display: flex; align-items: center; gap: 12px;
    font-size: 22px; color: var(--ink); height: 33.5px;
  }
  .benefits svg { width: 18px; height: 16px; flex: none; }

  .promise { position: absolute; left: 465px; top: 572px; color: var(--plum); }
  .promise .lead { font-size: 30px; font-weight: 900; line-height: 34px; letter-spacing: 0.2px; white-space: nowrap; }
  .promise .sub { font-size: 22px; color: var(--ink); line-height: 26px; white-space: nowrap; }

  .footer {
    position: absolute; left: 0; bottom: 0; width: 924px; height: 76px;
    background: var(--plum); display: flex; align-items: center;
    padding-left: 22px; color: var(--white);
  }
  .contact { display: flex; align-items: center; gap: 9px; font-weight: 600; white-space: nowrap; }
  .contact .icon {
    width: 34px; height: 34px; border-radius: 50%; background: var(--white);
    display: flex; align-items: center; justify-content: center; flex: none;
  }
  .contact.phone { font-size: 22px; letter-spacing: 0.4px; }
  .contact.web { font-size: 15.5px; margin-left: 16px; letter-spacing: 0; }
  .cta {
    position: absolute; left: 634px; top: 16px; width: 264px; height: 46px;
    background: var(--white); border-radius: 23px;
    display: flex; align-items: center; padding-left: 24px;
    color: var(--ink); font-size: 22px; font-weight: 800; text-decoration: none;
  }
  .cta .arrow {
    position: absolute; right: 6px; top: 5.5px; width: 35px; height: 35px;
    border-radius: 50%; background: var(--plum);
    display: flex; align-items: center; justify-content: center;
  }
</style>
</head>
<body>
<main class="ad">
  <svg class="ad-shapes" width="924" height="720" viewBox="0 0 924 720">
    <defs>
      <linearGradient id="hero-tone" x1="0" y1="0" x2="1" y2="1">
        <stop offset="0" stop-color="#c9b9a4"/>
        <stop offset="0.45" stop-color="#b49a86"/>
        <stop offset="1" stop-color="#d8cfc2"/>
      </linearGradient>
      <radialGradient id="inset-tone" cx="0.5" cy="0.45" r="0.6">
        <stop offset="0" stop-color="#a7a58a"/>
        <stop offset="1" stop-color="#4f6b3d"/>
      </radialGradient>
      <filter id="ring-shadow" x="-20%" y="-20%" width="140%" height="140%">
        <feDropShadow dx="0" dy="4" stdDeviation="5" flood-color="#000" flood-opacity="0.3"/>
      </filter>
    </defs>

    <rect class="hero-photo" x="200" y="0" width="724" height="430" fill="url(#hero-tone)"
          role="img" aria-label="Photo: smiling caregiver in plum scrubs sitting with a laughing elderly woman"/>

    <path class="swoosh" fill="var(--plum)"
          d="M0,0 L230,0 C390,10 470,130 520,240 C570,340 640,372 760,372 C830,372 880,364 924,352 L924,720 L0,720 Z"/>
    <path class="panel" fill="var(--white)"
          d="M0,166 C70,90 150,62 240,62 C340,62 420,120 470,210 C520,300 570,370 680,395 C780,415 860,410 924,398 L924,720 L0,720 Z"/>

    <ellipse class="blush-field" cx="720" cy="730" rx="450" ry="248" fill="var(--blush)"/>

    <circle class="inset-ring" cx="714" cy="442" r="118" fill="var(--plum)" filter="url(#ring-shadow)"/>
    <circle cx="714" cy="442" r="98" fill="var(--white)"/>
    <circle class="inset-photo" cx="714" cy="442" r="94" fill="url(#inset-tone)"
            role="img" aria-label="Photo: caregiver hugging a smiling elderly man in a wheelchair outdoors"/>

    <path class="accent-heart" fill="var(--heart-soft)"
          d="M853,560 C832,544 826,535 826,524 C826,515 833,508 842,508 C847,508 851,511 853,515 C855,511 859,508 864,508 C873,508 880,515 880,524 C880,535 874,544 853,560 Z"/>
  </svg>

  <div class="brand">
    <div class="brand-mark"></div>
    <div class="brand-name">
      <span class="primary">Meadowlark</span>
      <span class="secondary">Home Health Services</span>
    </div>
  </div>

  <h1 class="headline">Do you or your loved one<br>need <strong>CARE</strong> at home?</h1>

  <div class="rule top"></div>
  <p class="tagline">Live at home as long as possible!</p>
  <div class="rule bottom"></div>

  <ul class="benefits">
    <li><svg viewBox="0 0 18 16"><path fill="var(--plum)" d="M9,16 C2,10.5 0,8 0,4.8 C0,2 2,0 4.6,0 C6.4,0 8,1 9,2.6 C10,1 11.6,0 13.4,0 C16,0 18,2 18,4.8 C18,8 16,10.5 9,16 Z"/></svg>Caregivers You Can Trust</li>
    <li><svg viewBox="0 0 18 16"><path fill="var(--plum)" d="M9,16 C2,10.5 0,8 0,4.8 C0,2 2,0 4.6,0 C6.4,0 8,1 9,2.6 C10,1 11.6,0 13.4,0 C16,0 18,2 18,4.8 C18,8 16,10.5 9,16 Z"/></svg>Caregivers That Come On Time</li>
    <li><svg viewBox="0 0 18 16"><path fill="var(--plum)" d="M9,16 C2,10.5 0,8 0,4.8 C0,2 2,0 4.6,0 C6.4,0 8,1 9,2.6 C10,1 11.6,0 13.4,0 C16,0 18,2 18,4.8 C18,8 16,10.5 9,16 Z"/></svg>Caregivers That Live with You</li>
    <li><svg viewBox="0 0 18 16"><path fill="var(--plum)" d="M9,16 C2,10.5 0,8 0,4.8 C0,2 2,0 4.6,0 C6.4,0 8,1 9,2.6 C10,1 11.6,0 13.4,0 C16,0 18,2 18,4.8 C18,8 16,10.5 9,16 Z"/></svg>High Level Care</li>
    <li><svg viewBox="0 0 18 16"><path fill="var(--plum)" d="M9,16 C2,10.5 0,8 0,4.8 C0,2 2,0 4.6,0 C6.4,0 8,1 9,2.6 C10,1 11.6,0 13.4,0 C16,0 18,2 18,4.8 C18,8 16,10.5 9,16 Z"/></svg>Hours Match Your Needs</li>
  </ul>

  <div class="promise">
    <p class="lead">WE GIVE PEOPLE THE HELP</p>
    <p class="sub">They Need to live in the Place They Love</p>
  </div>

  <footer class="footer">
    <div class="contact phone">
      <span class="icon"><svg width="19" height="19" viewBox="0 0 24 24"><path fill="var(--plum)" d="M6.6 10.8c1.4 2.8 3.8 5.1 6.6 6.6l2.2-2.2c.3-.3.7-.4 1-.2 1.1.4 2.3.6 3.6.6.6 0 1 .4 1 1V20c0 .6-.4 1-1 1C10.6 21 3 13.4 3 4c0-.6.4-1 1-1h3.5c.6 0 1 .4 1 1 0 1.3.2 2.5.6 3.6.1.3 0 .7-.2 1l-2.3 2.2z"/></svg></span>
      555-014-2288
    </div>
    <div class="contact web">
      <span class="icon"><svg width="21" height="21" viewBox="0 0 24 24" fill="none" stroke="var(--plum)" stroke-width="1.8"><circle cx="12" cy="12" r="9"/><ellipse cx="12" cy="12" rx="4" ry="9"/><path d="M3 12h18M4.5 7.5h15M4.5 16.5h15"/></svg></span>
      WWW.MEADOWLARKHHS-EXAMPLE.COM
    </div>
    <a class="cta" href="https://www.meadowlarkhhs-example.com/">FIND OUT MORE
      <span class="arrow"><svg width="12" height="14" viewBox="0 0 12 14"><path fill="var(--white)" d="M2 1 L11 7 L2 13 Z"/></svg></span>
    </a>
  </footer>
</main>
</body>
</html>
```